Venture Traps Book Needs a Cover Design

We need a cover design for Venture Traps, Plain Guidance for Wobbly New Ventures and Stalled Company Founders. We will publish and ebook first (first priority), followed by a hard cover printed book, and then a soft cover book after a few months. The book includes 40 Venture Traps and actions owners can implement to counter them and grow. Some examples of killers: self-sabotage, wild optimism, scamming, addictions, burnout, no plan, procrastination, recklessness, haemorrhaging money, etc. We plan to publish the ebook to Readlo / Vendora standards. We want to see designs that convey professionalism, simplicity and creativity.

Target Market(s)

Small and microbusinesses, including start-ups, proprietorships, cottage industries, home-based, single operator, and businesses with or without employees, including corporations and partnerships with fewer than five employees

Industry/Entity Type

Business

Font styles to use
Sans Serif

Colors

Designer to choose colors to be used in the design.

Requirements
Must have
• Uncluttered, professional
• Title: Venture Traps
• Subtitle: Plain Guidance for Wobbly New Ventures and Stalled Company Founders
• Author: Miles Farquist
Nice to have
• n/a

```html
<!DOCTYPE html>
<html lang="en">
<head>
<meta charset="UTF-8">
<title>Venture Traps — Miles Farquist</title>
<link rel="stylesheet" href="https://fonts.googleapis.com/css2?family=Passion+One:wght@700&family=Exo+2:wght@200&family=Open+Sans:wght@400;600&display=swap">
<style>
  :root {
    --title-maroon: #2b0406;
    --title-navy: #16293d;
    --sky-top: #3f8fd6;
    --sky-mid: #8cc2ec;
    --horizon: #e9f3fa;
    --sea-light: #4d87b4;
    --sea-mid: #245784;
    --sea-deep: #0f2c4d;
    --sea-bottom: #0b2240;
    --text-light: #ffffff;
  }
  * { margin: 0; padding: 0; box-sizing: border-box; }
  html, body {
    width: 750px;
    height: 1200px;
    overflow: hidden;
    background: var(--sea-bottom);
  }
  .cover {
    position: relative;
    width: 750px;
    height: 1200px;
    overflow: hidden;
  }
  .cover-scene {
    position: absolute;
    inset: 0;
    background: linear-gradient(
      to bottom,
      var(--sky-top) 0%,
      var(--sky-mid) 20%,
      var(--horizon) 36.2%,
      var(--sea-light) 37%,
      var(--sea-mid) 50%,
      var(--sea-deep) 72%,
      var(--sea-bottom) 100%
    );
  }
  .title-block {
    position: absolute;
    top: 0;
    left: 0;
    width: 750px;
    height: 360px;
  }
  .title-art {
    display: block;
    width: 750px;
    height: 360px;
  }
  .title-main {
    font-family: "Passion One", "Arial Black", sans-serif;
    font-weight: 700;
    font-size: 152px;
    fill: var(--title-maroon);
  }
  .title-sub {
    font-family: "Exo 2", "Helvetica Neue", sans-serif;
    font-weight: 200;
    font-size: 168px;
    fill: var(--title-navy);
  }
  .subtitle {
    position: absolute;
    top: 932px;
    left: 40px;
    right: 40px;
    text-align: center;
    font-family: "Open Sans", Arial, sans-serif;
    font-weight: 400;
    font-size: 31px;
    line-height: 1.35;
    color: var(--text-light);
  }
  .author {
    position: absolute;
    top: 1064px;
    left: 0;
    right: 0;
    text-align: center;
    font-family: "Open Sans", Arial, sans-serif;
    font-weight: 600;
    font-size: 78px;
    line-height: 1;
    letter-spacing: 1px;
    color: var(--text-light);
    white-space: nowrap;
  }
</style>
</head>
<body>
  <main class="cover">
    <div class="cover-scene" role="img" aria-label="Bright blue sky with light clouds over a wide open ocean, an orange and white lifebuoy floating on the waves"></div>
    <h1 class="title-block" aria-label="Venture Traps">
      <svg class="title-art" viewBox="0 0 750 360" aria-hidden="true">
        <text class="title-main" x="48" y="194" textLength="658" lengthAdjust="spacingAndGlyphs">VENTURE</text>
        <text class="title-sub" x="51" y="332" textLength="657" lengthAdjust="spacing">TRAPS</text>
      </svg>
    </h1>
    <p class="subtitle">Plain Guidance for Wobbly New Ventures<br>and Stalled Company Founders</p>
    <p class="author">MILES FARQUIST</p>
  </main>
</body>
</html>
```